Brackenmoor.com.au - Quorvel Australia - Uncoded PSD only

We need a web design for a virtual assistant company based in Sydney Australia called "Brackenmoor". We provide virtual assistance and unlimited admin tasks to small business owners for a monthly fee. We would like to see designs that are not too different to www.quorvel.com. Words to describe the design and feel of this website are sleek and professional. We want to use bright inviting colours for the call to action buttons and a professional business focused background.

Target Market(s)

business executives, business owners, small business owners, those professionals who lack time.

Industry/Entity Type

Business Consultant

Number of Pages Required

3 page

Font styles to use
Sans Serif

Colors
5e5e5e
1b1b1b
3176b5
33b8a4

Requirements
Must have
• Call to action buttons, sleek business feel think plovix.io and quorvel.com
Nice to have
• Bold back ground colours, bright call to action buttons
Should not have
• too much white

```html
<!DOCTYPE html>
<html lang="en">
<head>
<meta charset="utf-8">
<title>Brackenmoor – Virtual Assistance</title>
<link href="https://fonts.googleapis.com/css2?family=Open+Sans:wght@400;600;700&display=swap" rel="stylesheet">
<style>
:root{
  --blue:#3176b5;
  --teal:#33b8a4;
  --ink:#1b1b1b;
  --grey:#5e5e5e;
  --light:#f4f4f4;
  --band:#d9d9d9;
  --footer:#1f1f1f;
  --footer-deep:#151515;
}
*{box-sizing:border-box;margin:0;padding:0}
html,body{width:679px;height:1200px;overflow:hidden;background:#fff}
body{font-family:"Open Sans",Arial,sans-serif;color:var(--grey)}
.page{width:679px;height:1200px;position:relative;overflow:hidden}

/* header */
.site-header{height:30px;display:flex;align-items:center;justify-content:space-between;padding:0 62px 0 62px;background:#fff}
.brand{font-weight:700;font-size:15px;color:var(--blue);letter-spacing:.5px}
.main-nav{display:flex;align-items:center;gap:14px;font-size:8px;color:var(--ink)}
.main-nav .active{color:var(--blue);font-weight:600}
.btn-search{background:var(--blue);color:#fff;padding:4px 16px;font-size:8px;border-radius:1px}

/* hero */
.hero{position:relative;height:254px;overflow:hidden}
.hero-photo{position:absolute;inset:0;background:radial-gradient(ellipse at 68% 40%,#2c5aa8 0,#1d3466 14%,#2b2b2b 36%,#1a1a1a 70%,#0f0f0f 100%)}
.hero-content{position:absolute;left:62px;top:95px;color:#fff}
.hero h1{font-size:21px;font-weight:700;margin-bottom:4px}
.hero p{font-size:9.5px;font-weight:600;line-height:1.35;width:330px}
.btn{display:inline-block;color:#fff;font-size:8.5px;border-radius:2px}
.btn-learn{background:var(--blue);padding:7px 20px;margin-top:14px}

/* services */
.services{height:262px;text-align:center;padding-top:24px;background:#fff}
.section-title{font-size:19px;font-weight:600;color:var(--ink)}
.title-rule{width:60px;height:1px;background:#999;margin:5px auto 8px}
.services .intro{font-size:5.5px;line-height:1.5;width:390px;margin:0 auto;color:#888}
.service-grid{display:flex;justify-content:center;gap:34px;margin-top:24px}
.service{width:96px}
.service svg{width:34px;height:34px}
.service h3{font-size:10px;font-weight:700;color:var(--ink);margin:8px 0 6px}
.service.featured h3{color:var(--teal)}
.service p{font-size:5.5px;line-height:1.55;color:#777}

/* consult */
.consult{position:relative;height:260px;overflow:hidden;text-align:center;color:#fff}
.consult-photo{position:absolute;inset:0;background:linear-gradient(100deg,#3a3a3a 0,#4b4d50 40%,#7b7f84 70%,#555 100%)}
.consult-shade{position:absolute;inset:0;background:rgba(20,20,20,.45)}
.consult-content{position:relative;padding-top:62px}
.consult h2{font-size:20px;font-weight:400}
.consult p{font-size:7px;width:400px;margin:4px auto 0;line-height:1.45}
.btn-consult{background:var(--blue);padding:9px 22px;font-size:11px;margin-top:16px}

/* testimonial */
.testimonial{position:relative;height:112px;text-align:center;background:#fff;padding-top:14px}
.avatar{width:38px;height:38px;border-radius:50%;margin:0 auto;background:linear-gradient(#d8c4b4,#a88e7c)}
.testimonial blockquote{font-size:8px;font-style:italic;line-height:1.45;width:300px;margin:8px auto 4px;color:var(--grey)}
.testimonial .name{font-size:6.5px;color:var(--blue);font-weight:600}
.testimonial .role{font-size:6px;color:var(--ink)}
.arrow{position:absolute;top:52px;width:24px;height:13px;background:var(--teal);display:flex;align-items:center;justify-content:center}
.arrow.prev{left:62px}.arrow.next{right:62px}

/* partners */
.partners{height:52px;background:var(--band);display:flex;align-items:center;justify-content:center;gap:24px}
.partner{width:70px;height:18px;background:#b3b3b3;border-radius:2px}

/* footer */
.site-footer{height:186px;background:var(--footer);color:#cfcfcf;display:flex;gap:22px;padding:16px 62px 0}
.col{width:120px}
.col h4{color:#fff;font-size:9px;font-weight:600;margin-bottom:10px}
.col p{font-size:5.5px;line-height:1.6}
.menu li{list-style:none;font-size:6px;line-height:2;display:flex;align-items:center;gap:5px}
.menu li.active{color:var(--teal)}
.contact li{list-style:none;display:flex;align-items:center;gap:7px;font-size:5.5px;margin-bottom:9px;line-height:1.4}
.ic{width:15px;height:15px;border:1px solid #888;border-radius:50%;flex:none;display:flex;align-items:center;justify-content:center}
.field{height:12px;background:#3a3a3a;font-size:5.5px;color:#aaa;padding:3px 6px;margin-bottom:5px}
.btn-submit{background:var(--blue);color:#fff;font-size:6px;padding:3px 10px;display:inline-block}
.bottom-bar{height:23px;background:var(--footer-deep);display:flex;align-items:center;justify-content:space-between;padding:0 62px;font-size:6px;color:#aaa}
.social{display:flex;gap:4px}
.social span{width:9px;height:9px;border-radius:50%;background:var(--blue)}
.social span:nth-child(3){background:#c0392b}
</style>
</head>
<body>
<div class="page">
  <header class="site-header">
    <div class="brand">BRACKENMOOR</div>
    <nav class="main-nav">
      <span class="active">Home</span><span>About Us</span><span>Service</span><span>Testimonial</span><span>Contact Us</span>
      <span class="btn-search">Search</span>
    </nav>
  </header>

  <section class="hero">
    <div class="hero-photo" role="img" aria-label="Dark photo of black umbrellas with one blue umbrella standing out"></div>
    <div class="hero-content">
      <h1>Welcome To BRACKENMOOR</h1>
      <p>Lorem ipsum dolor sit amet, consectetur adipiscing elit. Pellentesque tristique nisi at facilisis porta. Vivamus a est nisi. Suspendisse</p>
      <span class="btn btn-learn">Learn More</span>
    </div>
  </section>

  <section class="services">
    <h2 class="section-title">Our Service</h2>
    <div class="title-rule"></div>
    <p class="intro">If you have been stirring in backlinks, hidden in multiple accounts, do not worry! We can do that for you. If you already have one, we can improve your content and provide increased engagement with your audience.</p>
    <div class="service-grid">
      <div class="service">
        <svg viewBox="0 0 34 34"><rect x="5" y="13" width="24" height="17" fill="#3176b5"/><rect x="3" y="9" width="28" height="6" fill="#3176b5"/><rect x="15.5" y="9" width="3" height="21" fill="#fff"/><path d="M17 9c-3-6-9-5-7-1 1 2 5 1 7 1zm0 0c3-6 9-5 7-1-1 2-5 1-7 1z" fill="none" stroke="#3176b5" stroke-width="2"/></svg>
        <h3>Lorem ipsum dolor sit</h3>
        <p>Lorem ipsum dolor sit amet, consectetur adipiscing elit. Pellentesque tristique nisi at facilisis porta.</p>
      </div>
      <div class="service">
        <svg viewBox="0 0 34 34"><rect x="4" y="10" width="26" height="19" fill="#3176b5"/><path d="M4 10l13 10 13-10" fill="none" stroke="#fff" stroke-width="2"/><circle cx="17" cy="7" r="4" fill="none" stroke="#3176b5" stroke-width="2"/></svg>
        <h3>Lorem ipsum dolor sit</h3>
        <p>Lorem ipsum dolor sit amet, consectetur adipiscing elit. Pellentesque tristique nisi at facilisis porta.</p>
      </div>
      <div class="service featured">
        <svg viewBox="0 0 34 34"><rect x="9" y="4" width="22" height="18" fill="#33b8a4" transform="rotate(10 20 13)"/><rect x="3" y="11" width="22" height="18" fill="#fff" stroke="#33b8a4" stroke-width="2"/><path d="M5 27l7-8 5 5 3-3 4 6z" fill="#33b8a4"/><circle cx="19" cy="16" r="2" fill="#33b8a4"/></svg>
        <h3>Lorem ipsum dolor sit</h3>
        <p>Lorem ipsum dolor sit amet, consectetur adipiscing elit. Pellentesque tristique nisi at facilisis porta.</p>
      </div>
      <div class="service">
        <svg viewBox="0 0 34 34"><path d="M11 18l-4 13 5-3 3 4 3-11zM23 18l4 13-5-3-3 4-3-11z" fill="#3176b5"/><circle cx="17" cy="12" r="10" fill="#3176b5"/><circle cx="17" cy="12" r="5" fill="#fff"/></svg>
        <h3>Lorem ipsum dolor sit</h3>
        <p>Lorem ipsum dolor sit amet, consectetur adipiscing elit. Pellentesque tristique nisi at facilisis porta.</p>
      </div>
    </div>
  </section>

  <section class="consult">
    <div class="consult-photo" role="img" aria-label="Photo of business people working together at a laptop"></div>
    <div class="consult-shade"></div>
    <div class="consult-content">
      <h2>Lorem ipsum dolor sit amet onsectetur</h2>
      <p>Vivamus a est nisi. Suspendisse consectetur tortor ultrices, mollis dolor nec, commodo libero. Quisque porttitor augue lacus, id tempus sapien ullam corper</p>
      <span class="btn btn-consult">Request A Consultation</span>
    </div>
  </section>

  <section class="testimonial">
    <div class="avatar" role="img" aria-label="Portrait of the client giving the testimonial"></div>
    <blockquote>Lorem ipsum dolor sit amet, consectetur adipiscing elit. Proin ut ultricies dui. Nullam sagittis commodo mi nec</blockquote>
    <div class="name">Marla Venn</div>
    <div class="role">Designer</div>
    <span class="arrow prev"><svg width="8" height="8" viewBox="0 0 8 8"><path d="M6 1L2 4l4 3" fill="none" stroke="#fff" stroke-width="1.5"/></svg></span>
    <span class="arrow next"><svg width="8" height="8" viewBox="0 0 8 8"><path d="M2 1l4 3-4 3" fill="none" stroke="#fff" stroke-width="1.5"/></svg></span>
  </section>

  <section class="partners" aria-label="Partners">
    <span class="partner"></span><span class="partner"></span><span class="partner"></span><span class="partner"></span><span class="partner"></span><span class="partner"></span>
  </section>

  <footer class="site-footer">
    <div class="col">
      <h4>About us</h4>
      <p>Brackenmoor connects busy owners with the best team of Australian virtual assistants. We take on the unlimited admin tasks that slow your business down, so you can focus on growth, clients and the work that matters most to you every day.</p>
    </div>
    <div class="col">
      <h4>Main menu</h4>
      <ul class="menu">
        <li>› Home</li><li>› About Us</li><li>› Service</li><li class="active">› Testimonial</li><li>› Contact Us</li>
      </ul>
    </div>
    <div class="col">
      <h4>Contact Us</h4>
      <ul class="contact">
        <li><span class="ic"><svg width="7" height="8" viewBox="0 0 7 8"><path d="M3.5 8S1 5 1 3a2.5 2.5 0 015 0c0 2-2.5 5-2.5 5z" fill="#ccc"/></svg></span>Level 4, 120 Harbour Lane<br>Sydney NSW 2000</li>
        <li><span class="ic"><svg width="7" height="7" viewBox="0 0 7 7"><path d="M1 1h2l1 2-1 1a4 4 0 002 2l1-1 1 1v1c-4 0-7-3-7-6z" fill="#ccc"/></svg></span>(02) 5550 1842</li>
        <li><span class="ic"><svg width="8" height="6" viewBox="0 0 8 6"><rect x=".5" y=".5" width="7" height="5" fill="none" stroke="#ccc"/><path d="M.5.5L4 3.5 7.5.5" fill="none" stroke="#ccc"/></svg></span>hello@brackenmoor.com.au</li>
      </ul>
    </div>
    <div class="col">
      <h4>Newsletter</h4>
      <div class="field">Name</div>
      <div class="field">Email</div>
      <span class="btn-submit">Submit</span>
    </div>
  </footer>
  <div class="bottom-bar">
    <span>Copyright © 2015 brackenmoor.com.au</span>
    <span class="social"><span></span><span></span><span></span><span></span></span>
  </div>
</div>
</body>
</html>
```